Business Card Design Project

Please create a custom business card for Plume tallying. The logo is attached to this brief.

Questions can be posted on the Discussion Board.

Address :
CEO : Gerhard Moulin
Mobile : +33641927058
9 rue Vasselot
75014 Paris
France

Reason: Sorry wrong logo. I will update asap

Hi, Sorry, I post the wrong file. I just update the correct logo. If you can integrate some charts as background it will be nice

Hi Everybody Please make it beautifull, clean, soft like quince designs does to create their product. I want somewhere to show in a beautifull way some datavisualization charts. Not to much, but try to find a way to design it beautifull with less. Get inspire by datavisualization : http://www.brovaxkit.com/27841-neat-vector-chart-and-graph-layout-pieces-07/

Target Market(s)

B to B
Customers are accountant, CPA, finance departement

Industry/Entity Type

Business

Font styles to use
Sans Serif

Requirements
Must have
• I want to give a clear message about what we do. We do dashboards, we create beautifull charts
Nice to have
• displays charts icons to let people know tha we do charts

```html
<!DOCTYPE html>
<html lang="en">
<head>
<meta charset="utf-8">
<title>Plume tallying – business card</title>
<link rel="stylesheet" href="https://fonts.googleapis.com/css2?family=Ubuntu:wght@400;500;700&display=swap">
<style>
  :root {
    --page: #e9eaec;
    --card-dark: #231f20;
    --card-dark-shade: #1b1819;
    --band: #e3e4e6;
    --brand-blue: #1aa3e8;
    --sky-light: #eaf6fd;
    --sky-mid: #bfe4f8;
    --sky-deep: #8fd0f3;
    --ink: #3a3a3c;
    --ink-soft: #6d6e70;
    --text-light: #f1f1f1;
    --text-muted: #b9b9bb;
  }
  * { box-sizing: border-box; margin: 0; padding: 0; }
  html, body { width: 1200px; height: 1000px; overflow: hidden; }
  body {
    background: var(--page);
    font-family: "Ubuntu", sans-serif;
    position: relative;
  }
  .card {
    position: absolute;
    top: 350px;
    width: 520px;
    height: 300px;
    border-radius: 4px;
    overflow: hidden;
    box-shadow: 0 10px 28px rgba(0,0,0,.18);
  }
  .card svg.card-bg { position: absolute; inset: 0; }
  .card--front { left: 50px; background: var(--card-dark); }
  .card--back { left: 630px; background: var(--sky-light); }

  .brand-lockup {
    position: absolute;
    display: flex;
    flex-direction: column;
    align-items: flex-end;
  }
  .brand {
    display: flex;
    align-items: center;
    gap: 10px;
  }
  .brand-mark { width: 22px; height: 22px; background: var(--brand-blue); flex: none; }
  .brand-name { font-weight: 400; color: var(--ink); line-height: 1; }
  .brand-tagline {
    color: var(--ink-soft);
    font-size: 9px;
    letter-spacing: .3px;
    margin-top: 6px;
  }

  .card--front .brand-lockup { left: 70px; top: 52px; }
  .card--front .brand-name { font-size: 28px; }

  .contact {
    position: absolute;
    left: 190px;
    top: 150px;
    color: var(--text-muted);
    font-size: 14px;
    line-height: 1.5;
  }
  .contact-name { color: var(--text-light); font-weight: 700; font-size: 19px; }
  .contact-role { color: var(--text-light); font-size: 14px; margin-bottom: 8px; }
  .contact-row { display: grid; grid-template-columns: 70px 12px auto; }

  .card--back .brand-lockup { left: 50%; top: 50%; transform: translate(-50%, -50%); }
  .card--back .brand { gap: 12px; }
  .card--back .brand-mark { width: 28px; height: 28px; }
  .card--back .brand-name { font-size: 40px; }
  .card--back .brand-tagline { font-size: 11px; margin-top: 8px; }
</style>
</head>
<body>

<section class="card card--front" aria-label="Card front">
  <svg class="card-bg" width="520" height="300" viewBox="0 0 520 300" aria-hidden="true">
    <polygon points="0,300 150,150 300,300" fill="var(--card-dark-shade)"/>
    <polygon points="260,300 400,160 520,280 520,300" fill="var(--card-dark-shade)"/>
    <polygon points="0,20 520,20 520,120 0,120" fill="var(--band)"/>
    <polygon points="0,20 60,20 0,60" fill="var(--brand-blue)"/>
    <polygon points="520,120 440,120 520,80" fill="var(--brand-blue)"/>
  </svg>
  <div class="brand-lockup">
    <div class="brand">
      <span class="brand-mark"></span>
      <span class="brand-name">Plume tallying</span>
    </div>
    <span class="brand-tagline">visualize your data</span>
  </div>

  <div class="contact">
    <div class="contact-name">Gerhard Moulin</div>
    <div class="contact-role">CEO</div>
    <div class="contact-row"><span>Mobile</span><span>:</span><span>+33641927058</span></div>
    <div class="contact-row"><span>Address</span><span>:</span><span>9 rue Vasselot</span></div>
    <div class="contact-row"><span></span><span></span><span>75014 Paris</span></div>
    <div class="contact-row"><span></span><span></span><span>France</span></div>
  </div>
</section>

<section class="card card--back" aria-label="Card back">
  <svg class="card-bg" width="520" height="300" viewBox="0 0 520 300" aria-hidden="true">
    <defs>
      <radialGradient id="sky" cx="50%" cy="50%" r="65%">
        <stop offset="0" stop-color="#ffffff"/>
        <stop offset=".6" stop-color="var(--sky-light)"/>
        <stop offset="1" stop-color="var(--sky-mid)"/>
      </radialGradient>
    </defs>
    <rect width="520" height="300" fill="url(#sky)"/>
    <polygon points="0,0 140,0 0,90" fill="var(--brand-blue)" opacity=".55"/>
    <polygon points="520,300 380,300 520,210" fill="var(--brand-blue)" opacity=".55"/>
  </svg>
  <svg class="card-bg" width="520" height="300" viewBox="0 0 520 300" role="img" aria-label="Soft band where a decorative line-chart pattern belongs">
    <defs>
      <linearGradient id="band-left" x1="0" y1="0" x2="1" y2="0">
        <stop offset="0" stop-color="var(--sky-deep)" stop-opacity=".55"/>
        <stop offset="1" stop-color="var(--sky-deep)" stop-opacity="0"/>
      </linearGradient>
      <linearGradient id="band-right" x1="1" y1="0" x2="0" y2="0">
        <stop offset="0" stop-color="var(--sky-deep)" stop-opacity=".55"/>
        <stop offset="1" stop-color="var(--sky-deep)" stop-opacity="0"/>
      </linearGradient>
    </defs>
    <polygon points="0,120 70,120 100,300 0,300" fill="url(#band-left)"/>
    <polygon points="420,0 520,0 520,180 450,180" fill="url(#band-right)"/>
  </svg>
  <div class="brand-lockup">
    <div class="brand">
      <span class="brand-mark"></span>
      <span class="brand-name">Plume tallying</span>
    </div>
    <span class="brand-tagline">visualize your data</span>
  </div>
</section>

</body>
</html>
```